Business Card design for new private practice opening

I need a business card design for my new private practice with my new logo uploaded as a file
On the front the logo
On the back: maybe a small logo somewhere?
Priv. Doz. DDr. Corinna Vestaluk
Fachärztin für Allgemein- & Viszeralchirurgie
Address: xxx
Tel: xxx
Mobil:xxx
Webseite:xxx
Email:xxx

Contact Information for Business Card

See project description above for details

Requirements
Nice to have
• I would like the colors of the logo incorporated into the business card

```html
<!DOCTYPE html>
<html lang="de">
<head>
<meta charset="utf-8">
<title>Vestaluk Chirurgie – Visitenkarte</title>
<link href="https://fonts.googleapis.com/css2?family=Montserrat:wght@400;500;700&display=swap" rel="stylesheet">
<style>
  :root {
    --bg: #ecebe8;
    --card: #ffffff;
    --teal: #4dbab4;
    --grey-brand: #7f7f7f;
    --grey-text: #5f5f5f;
    --ink: #3d3d3d;
  }
  * { box-sizing: border-box; margin: 0; padding: 0; }
  html, body {
    width: 967px; height: 1200px; overflow: hidden;
    background: var(--bg);
    font-family: "Montserrat", Arial, sans-serif;
  }
  .card {
    position: absolute; left: 167px; width: 639px; height: 412px;
    background: var(--card);
  }
  .card--front { top: 143px; }
  .card--back { top: 645px; }

  .brand {
    position: absolute; left: 85px; top: 129px;
    display: flex; align-items: center; gap: 14px;
  }
  .brand__dot {
    width: 136px; height: 136px; border-radius: 50%;
    background: var(--teal);
  }
  .brand__name {
    font-weight: 700; font-size: 51px; line-height: 1.1;
    color: var(--grey-brand); letter-spacing: 0.5px;
  }
  .stripe { position: absolute; left: 0; right: 0; background: var(--teal); }
  .stripe--thin { top: 366px; height: 2px; }
  .stripe--thick { top: 372px; height: 7px; }

  .back__dot {
    position: absolute; left: 263px; top: 42px;
    width: 112px; height: 112px; border-radius: 50%;
    background: var(--teal);
  }
  .holder {
    position: absolute; left: 0; right: 0; top: 183px;
    text-align: center; font-size: 29px; line-height: 36px; font-weight: 500;
    color: var(--grey-text);
  }
  .specialty {
    position: absolute; left: 0; right: 0; top: 224px;
    text-align: center; font-size: 19px; line-height: 24px; color: var(--ink);
  }
  .contact {
    position: absolute; display: flex; flex-direction: column; gap: 10px;
    list-style: none; font-size: 20px; color: var(--ink);
  }
  .contact--left { left: 121px; top: 280px; }
  .contact--right { left: 359px; top: 280px; }
  .contact li { display: flex; align-items: center; gap: 9px; height: 24px; }
  .contact svg { width: 24px; height: 24px; flex: none; }
</style>
</head>
<body>
  <section class="card card--front">
    <div class="brand">
      <div class="brand__dot"></div>
      <div class="brand__name">VESTALUK<br>CHIRURGIE</div>
    </div>
    <div class="stripe stripe--thin"></div>
    <div class="stripe stripe--thick"></div>
  </section>

  <section class="card card--back">
    <div class="back__dot"></div>
    <h1 class="holder">Priv. Doz. DDr. Corinna Vestaluk</h1>
    <p class="specialty">Fachärztin für Allgemein- &amp; Viszeralchirurgie</p>

    <ul class="contact contact--left">
      <li>
        <svg viewBox="0 0 24 24"><circle cx="12" cy="12" r="12" fill="var(--teal)"/><path d="M12 5.5a4.3 4.3 0 0 0-4.3 4.3c0 3.2 4.3 8.2 4.3 8.2s4.3-5 4.3-8.2A4.3 4.3 0 0 0 12 5.5z" fill="#fff"/><circle cx="12" cy="9.8" r="1.6" fill="var(--teal)"/></svg>
        Address: xxx
      </li>
      <li>
        <svg viewBox="0 0 24 24"><circle cx="12" cy="12" r="12" fill="var(--teal)"/><path d="M8.3 6.2l2 2.2-1.2 1.6c.8 1.8 2.2 3.2 4 4l1.6-1.2 2.2 2-.9 2.1c-4.7-.4-8.5-4.2-8.9-8.9z" fill="#fff"/></svg>
        Tel: xxx
      </li>
      <li>
        <svg viewBox="0 0 24 24"><circle cx="12" cy="12" r="12" fill="var(--teal)"/><rect x="8.5" y="5.5" width="7" height="13" rx="1.3" fill="none" stroke="#fff" stroke-width="1.5"/><circle cx="12" cy="16.2" r=".8" fill="#fff"/></svg>
        Mobil: xxx
      </li>
    </ul>

    <ul class="contact contact--right">
      <li>
        <svg viewBox="0 0 24 24"><circle cx="12" cy="12" r="12" fill="var(--teal)"/><g fill="none" stroke="#fff" stroke-width="1.2"><circle cx="12" cy="12" r="6"/><ellipse cx="12" cy="12" rx="2.6" ry="6"/><path d="M6 12h12M7 9h10M7 15h10"/></g></svg>
        Webseite: xxx
      </li>
      <li>
        <svg viewBox="0 0 24 24"><circle cx="12" cy="12" r="12" fill="var(--teal)"/><rect x="6" y="8" width="12" height="8.5" fill="#fff"/><path d="M6 8l6 5 6-5" fill="none" stroke="var(--teal)" stroke-width="1.2"/></svg>
        Email: xxx
      </li>
    </ul>
  </section>
</body>
</html>
```